Event Ticketing Website & Logo

We are looking for a fresh, creative and fun looking website where both customers can login and promoters of events can login and post there events. we want to create a brand where people know "Gatepass Pro" and find some of the best tickets and exclusive tickets to an amazing selection of events.

We need the customers to register with either zorblix or pindora so we need to incorporate two login sections one for the consumer and one for the promoter to login and upload there events.

The design needs to be fresh, modern, fun, and show case some form of exclusivity signup.

we are looking for a logo that incorporates some form of location marker, or some form related to getting in. "Gatepass Pro" "Gatepass Pro.com"

The logo is a mock up and we are open to designs that will reflect the logo.

Target Market(s)

example websites we like
https://www.plantheeve.example/london
https://www.showrally.example.uk/

Our Target Audience is from anyone of 16 years of age up to 80 years of age. this is a very general

Logo Text

GatepassPro.com

Number of Pages Required

1 page

Font styles to use
Sans Serif

Colors

Designer to choose colors to be used in the design.

Requirements
Must have
• This website has to show customer reviews on the home page like - https://www.harfordquill.example.uk/estate-agent-in-epping/ you will see customer reviews from vouch ledger.
• We need to incorporate social media links - Pindora, Chirvex, Snaplorn, Workvane
Nice to have
• Pictures of events such as ice hockey, music festivals, baseball, Theater events, rugby events, football events, family festivals, Car Shows, and would be good to show it like they have done on this website - https://www.showrally.example.uk/
• Categories like; Top Music Events, Top Comedy, Top Theater Shows, Top Sporting Events, Top Family Attractions.

```html
<!DOCTYPE html>
<html lang="en">
<head>
<meta charset="utf-8">
<title>Gatepass Pro – Discover. Book. Enjoy.</title>
<link href="https://fonts.googleapis.com/css2?family=Raleway:wght@600;700;800&family=Open+Sans:wght@400;600;700&display=swap" rel="stylesheet">
<style>
:root{
  --orange:#f26522;
  --orange-dark:#d9500f;
  --ink:#1c1c1c;
  --text:#555555;
  --muted:#8a8a8a;
  --white:#ffffff;
  --light:#efedee;
  --dark:#141414;
  --hero-a:#2b0d0d;
  --hero-b:#0f3c44;
}
*{box-sizing:border-box;margin:0;padding:0}
html,body{width:1200px;height:3888px;overflow:hidden}
body{font-family:"Open Sans",Arial,sans-serif;color:var(--text);background:var(--white);position:relative}
h1,h2,h3,h4{font-family:"Raleway",Arial,sans-serif;color:var(--ink)}
.abs{position:absolute}
.btn{display:inline-flex;align-items:center;gap:10px;background:var(--orange);color:var(--white);font-size:13px;font-weight:600;border-radius:3px;padding:8px 18px;white-space:nowrap}
.brand{display:flex;align-items:center;gap:10px;font-family:"Raleway",Arial,sans-serif;font-weight:800;font-size:26px;color:var(--white);white-space:nowrap}
.brand .dot{width:24px;height:24px;border-radius:50%;background:var(--orange);flex:none}

/* header + hero */
.hero{position:absolute;left:0;top:0;width:1200px;height:540px;background:radial-gradient(circle at 30% 45%,#b3262a 0%,transparent 40%),radial-gradient(circle at 80% 40%,#1f7b85 0%,transparent 45%),linear-gradient(180deg,#1a0f12,var(--hero-a) 55%,#120607)}
.hero::after{content:"";position:absolute;inset:0;background:linear-gradient(180deg,rgba(0,0,0,.55),rgba(0,0,0,.25) 60%,rgba(0,0,0,.6))}
.nav{position:absolute;left:0;top:0;width:1200px;height:72px;display:flex;align-items:center;padding:0 160px;z-index:2;gap:20px}
.nav .brand{margin-right:auto;font-size:22px}
.nav a{color:var(--white);font-size:13px;text-decoration:none;white-space:nowrap}
.nav a.active{background:var(--orange);padding:5px 12px;border-radius:3px}
.nav svg{flex:none}
.nav .auth{display:flex;gap:6px;flex:none}
.nav .auth span{background:var(--orange);color:var(--white);font-size:11px;padding:4px 10px;border-radius:2px;white-space:nowrap}
.hero-copy{position:absolute;left:0;top:120px;width:1200px;text-align:center;z-index:2}
.hero-copy h1{color:var(--white);font-size:58px;font-weight:800;letter-spacing:1px}
.hero-copy p{color:#e6e6e6;font-size:14px;line-height:1.5;width:560px;margin:12px auto 0}
.search{position:absolute;left:220px;top:266px;width:760px;display:flex;gap:12px;z-index:2}
.search .field{flex:1;height:34px;background:rgba(20,20,20,.8);border:1px solid #444;color:#ddd;font-size:12px;display:flex;align-items:center;justify-content:space-between;padding:0 12px}
.search-btn{position:absolute;left:720px;top:318px;width:260px;height:34px;justify-content:center;z-index:2}
.hero-dots{position:absolute;left:580px;top:484px;display:flex;gap:8px;z-index:2}
.hero-dots i{width:8px;height:8px;border-radius:50%;background:rgba(255,255,255,.5)}
.hero-dots i:first-child{background:var(--orange)}

/* section heads */
.sec-head{position:absolute;left:192px;width:816px}
.sec-head h2{font-size:40px;font-weight:700}
.sec-head p{font-size:13px;line-height:1.6;width:500px;margin-top:6px}
.sec-head .btn{position:absolute;right:0;top:10px;font-size:12px;padding:6px 16px}

/* event cards */
.card{position:absolute;width:200px;height:220px;border-radius:8px;overflow:hidden;background:linear-gradient(180deg,#5a5a5a,#262626)}
.card .meta{position:absolute;left:0;bottom:0;width:100%;padding:14px;background:linear-gradient(180deg,transparent,rgba(242,101,34,.95) 45%)}
.card h4{color:var(--white);font-size:13px;font-weight:700;white-space:nowrap}
.card small{display:block;color:#fff;font-size:11px;margin-top:2px}
.card .stars{color:#fff;font-size:11px;letter-spacing:2px;margin-top:3px}
.card.featured{background:var(--orange);height:240px;text-align:center;color:var(--white);padding:24px 18px}
.card.featured h4{font-size:16px}
.card.featured p{font-size:11px;line-height:1.5;margin-top:10px;color:#fff}
.card.featured .view{position:absolute;left:0;bottom:0;width:100%;padding:14px;background:var(--orange-dark);font-size:12px;font-weight:600}
.arrows{position:absolute;left:560px;display:flex;gap:6px}

/* newsletter */
.newsletter{position:absolute;left:0;top:1688px;width:1200px;height:332px;background:linear-gradient(90deg,#2a1d17,#3d2a22 50%,#1c1614);text-align:center}
.newsletter::after{content:"";position:absolute;inset:0;background:rgba(0,0,0,.55)}
.newsletter>*{position:relative;z-index:1}
.newsletter h2{color:var(--white);font-size:38px;padding-top:50px}
.newsletter p{color:#ddd;font-size:13px;width:520px;margin:10px auto 0;line-height:1.6}
.subscribe{display:flex;width:560px;margin:26px auto 0}
.subscribe .input{flex:1;height:40px;background:var(--white);color:#777;font-size:12px;display:flex;align-items:center;padding:0 16px}
.subscribe .btn{border-radius:0;padding:0 26px;font-size:12px}
.socials{display:flex;justify-content:center;gap:14px;margin-top:28px}
.socials span{color:var(--white);font-size:11px;font-weight:600;border:1px solid rgba(255,255,255,.5);border-radius:50%;width:30px;height:30px;display:flex;align-items:center;justify-content:center}

/* categories */
.cat-head{position:absolute;left:0;top:2060px;width:1200px;text-align:center}
.cat-head h2{font-size:40px}
.cat-head p{font-size:13px;width:560px;margin:10px auto 0;line-height:1.6}
.hexes{position:absolute;left:0;top:2190px}

/* reviews */
.reviews{position:absolute;left:0;top:2496px;width:1200px;height:416px;background:var(--light)}
.vouch{position:absolute;left:200px;top:190px}
.vouch .name{font-family:"Raleway",Arial,sans-serif;font-weight:800;font-size:36px;color:var(--ink);display:flex;align-items:center;gap:10px;white-space:nowrap}
.vouch .name i{width:22px;height:22px;border-radius:50%;background:var(--orange);flex:none}
.vouch .score{margin-top:10px;font-size:26px;color:var(--orange);letter-spacing:4px}
.vouch .total{margin-top:8px;font-size:13px;color:var(--ink)}
.review{position:absolute;top:164px;width:196px;height:220px;background:var(--white);box-shadow:0 4px 14px rgba(0,0,0,.12);text-align:center;padding:16px 14px}
.review .avatar{width:40px;height:40px;border-radius:50%;margin:0 auto;background:linear-gradient(135deg,#c9a48a,#7a5a48)}
.review h4{font-size:13px;margin-top:8px}
.review .rate{color:var(--orange);font-size:12px;letter-spacing:2px;margin-top:4px}
.review p{font-size:10px;line-height:1.5;margin-top:6px}
.review .more{font-size:10px;color:var(--orange);font-weight:700;margin-top:8px}
.chev{position:absolute;top:264px;color:#666;font-size:20px}

/* about */
.about{position:absolute;left:192px;top:2970px;width:450px}
.about h2{font-size:34px;line-height:1.25;font-weight:800}
.about p{font-size:11px;line-height:1.7;margin-top:16px}
.about .btn{margin-top:24px}
.about-frame{position:absolute;left:736px;top:3010px;width:270px;height:410px;background:var(--orange);border-radius:6px}
.about-photo{position:absolute;left:712px;top:2984px;width:272px;height:410px;border-radius:6px;background:linear-gradient(160deg,#e8e2dd,#bfb3aa 55%,#6d5c52)}

/* footer */
.footer{position:absolute;left:0;top:3432px;width:1200px;height:456px;background:radial-gradient(circle at 70% 20%,#5a3a1c,transparent 50%),linear-gradient(180deg,#2a1f16,var(--dark))}
.footer::after{content:"";position:absolute;inset:0;background:rgba(0,0,0,.45)}
.footer>*{position:relative;z-index:1}
.footer .brand{position:absolute;left:0;width:1200px;justify-content:center;top:44px;font-size:32px}
.footer h3{position:absolute;color:var(--white);font-size:30px;font-weight:600;top:150px;white-space:nowrap}
.links{position:absolute;top:210px;list-style:none}
.links li{color:#ddd;font-size:10px;line-height:2.1;text-transform:uppercase;white-space:nowrap}
.contact{position:absolute;left:800px;top:206px;list-style:none}
.contact li{display:flex;align-items:center;gap:10px;color:#ddd;font-size:11px;margin-bottom:14px;white-space:nowrap}
.contact svg{flex:none}
.fsocial{position:absolute;left:840px;top:330px;display:flex;gap:8px}
.fsocial span{font-size:10px;color:#fff;background:var(--orange);border-radius:50%;width:24px;height:24px;display:flex;align-items:center;justify-content:center;font-weight:700}
.copy{position:absolute;left:0;bottom:0;width:1200px;border-top:1px solid rgba(255,255,255,.15);height:40px;display:flex;align-items:center;justify-content:center;color:#bbb;font-size:10px}
.copy b{color:var(--orange);font-weight:600;margin:0 4px}
</style>
</head>
<body>

<!-- header & hero -->
<section class="hero" role="img" aria-label="Concert crowd with raised hands under red and teal stage lights">
  <nav class="nav">
    <div class="brand"><span class="dot"></span>Gatepass Pro</div>
    <a class="active">Home</a>
    <a>Trending Events</a>
    <a>Hot Tickets</a>
    <a>Best Reviews</a>
    <a>Contact Us</a>
    <svg width="14" height="14" viewBox="0 0 14 14"><circle cx="6" cy="6" r="4.5" fill="none" stroke="#fff" stroke-width="1.6"/><path d="M9.5 9.5l3.5 3.5" stroke="#fff" stroke-width="1.6"/></svg>
    <div class="auth"><span>Login</span><span>Promoter</span></div>
  </nav>
  <div class="hero-copy">
    <h1>DISCOVER. BOOK. ENJOY.</h1>
    <p>Lorem Ipsum is simply dummy text of the printing and typesetting industry. Lorem Ipsum has been the industry's standard dummy text ever since the 1500s.</p>
  </div>
  <div class="search">
    <div class="field">Select Event <span>▾</span></div>
    <div class="field">Select Date <span>▾</span></div>
    <div class="field">Select City <span>▾</span></div>
  </div>
  <div class="btn search-btn">Search Events</div>
  <div class="hero-dots"><i></i><i></i><i></i></div>
</section>

<!-- trending events -->
<div class="sec-head" style="top:612px">
  <h2>Trending Events</h2>
  <p>Lorem Ipsum is simply dummy text of the printing and typesetting industry. Lorem Ipsum has been the industry's standard dummy text ever since the 1500s.</p>
  <span class="btn">View All →</span>
</div>
<div class="abs" style="left:0;top:730px;width:1200px;height:280px;overflow:hidden">
  <div class="card" style="left:192px;top:30px" role="img" aria-label="Baseball stadium at dusk"><div class="meta"><h4>Event Name Awaited</h4><small>Tickets from £ 35.00</small><div class="stars">★★★★★</div></div></div>
  <div class="card" style="left:406px;top:30px;background:linear-gradient(180deg,#8a7060,#2c241f)" role="img" aria-label="Rugby players in a scrum"><div class="meta"><h4>Event Name Awaited</h4><small>Tickets from £ 35.00</small><div class="stars">★★★★★</div></div></div>
  <div class="card featured" style="left:620px;top:10px">
    <h4>Event Name</h4>
    <p>Tickets from £ 35.00<br>★★★★★</p>
    <p><svg width="14" height="18" viewBox="0 0 14 18"><path d="M7 1a6 6 0 0 0-6 6c0 4.5 6 10 6 10s6-5.5 6-10a6 6 0 0 0-6-6z" fill="#fff"/><circle cx="7" cy="7" r="2.2" fill="#f26522"/></svg><br>Event At Some Location<br>Friendly Hall, Main Street</p>
    <div class="view">View Details →</div>
  </div>
  <div class="card" style="left:834px;top:30px;background:linear-gradient(180deg,#3b3b3b,#121212)" role="img" aria-label="Baseball in a catcher's glove"><div class="meta"><h4>Event Name Awaited</h4><small>Tickets from £ 35.00</small><div class="stars">★★★★★</div></div></div>
  <div class="card" style="left:1048px;top:30px;background:linear-gradient(180deg,#6a1e22,#1e0c0d)" role="img" aria-label="American football player in red helmet"><div class="meta"><h4>Event Name Awaited</h4><small>Tickets from £ 35.00</small><div class="stars">★★★★★</div></div></div>
</div>
<svg class="arrows" style="top:1058px" width="80" height="30" viewBox="0 0 80 30"><path d="M40 8H72M64 2l8 6-8 6" stroke="#f26522" stroke-width="2.5" fill="none"/><path d="M40 22H8M16 16l-8 6 8 6" stroke="#1c1c1c" stroke-width="2.5" fill="none"/></svg>

<!-- hot tickets -->
<div class="sec-head" style="top:1152px">
  <h2>Hot Tickets</h2>
  <p>Lorem Ipsum is simply dummy text of the printing and typesetting industry. Lorem Ipsum has been the industry's standard dummy text ever since the 1500s.</p>
  <span class="btn">View All →</span>
</div>
<div class="abs" style="left:0;top:1284px;width:1200px;height:260px;overflow:hidden">
  <div class="card" style="left:192px;top:0;height:256px;background:linear-gradient(180deg,#4a4a4a,#161616)" role="img" aria-label="Ice hockey player on the rink"><div class="meta"><h4>Event Name Awaited</h4><small>Tickets from £ 35.00</small><div class="stars">★★★★★</div></div></div>
  <div class="card" style="left:406px;top:0;height:256px;background:linear-gradient(180deg,#7a2528,#1d0b0c)" role="img" aria-label="Football player in red helmet"><div class="meta"><h4>Event Name Awaited</h4><small>Tickets from £ 35.00</small><div class="stars">★★★★★</div></div></div>
  <div class="card" style="left:620px;top:0;height:256px;background:linear-gradient(180deg,#8a3a2a,#281412)" role="img" aria-label="Music festival crowd at night"><div class="meta"><h4>Event Name Awaited</h4><small>Tickets from £ 35.00</small><div class="stars">★★★★★</div></div></div>
  <div class="card" style="left:834px;top:0;height:256px;background:linear-gradient(180deg,#8f8f8f,#2e2e2e)" role="img" aria-label="Baseball field seen from the stands"><div class="meta"><h4>Event Name Awaited</h4><small>Tickets from £ 35.00</small><div class="stars">★★★★★</div></div></div>
  <div class="card" style="left:1048px;top:0;height:256px;background:linear-gradient(180deg,#5b4337,#1a1210)" role="img" aria-label="Rugby match tackle"><div class="meta"><h4>Event Name Awaited</h4><small>Tickets from £ 35.00</small><div class="stars">★★★★★</div></div></div>
</div>
<svg class="arrows" style="top:1580px" width="80" height="30" viewBox="0 0 80 30"><path d="M40 8H72M64 2l8 6-8 6" stroke="#f26522" stroke-width="2.5" fill="none"/><path d="M40 22H8M16 16l-8 6 8 6" stroke="#1c1c1c" stroke-width="2.5" fill="none"/></svg>

<!-- newsletter -->
<section class="newsletter" role="img" aria-label="Audience seated in a dimly lit theatre">
  <h2>Subscribe Our Newsletter</h2>
  <p>Lorem Ipsum is simply dummy text of the printing and typesetting industry. Lorem Ipsum has been the industry's standard dummy text ever since the 1500s.</p>
  <div class="subscribe"><div class="input">Enter Your Email Address</div><span class="btn">SUBSCRIBE</span></div>
  <div class="socials"><span>P</span><span>C</span><span>W</span><span>S</span></div>
</section>

<!-- top categories -->
<div class="cat-head">
  <h2>Top Categories</h2>
  <p>Lorem Ipsum is simply dummy text of the printing and typesetting industry. Lorem Ipsum has been the industry's standard dummy text ever since the 1500s.</p>
</div>
<svg class="hexes" width="1200" height="220" viewBox="0 0 1200 220" font-family="Raleway, Arial, sans-serif" font-weight="700" font-size="13" fill="#fff" text-anchor="middle">
  <defs>
    <linearGradient id="hMusic" x1="0" y1="0" x2="0" y2="1"><stop offset="0" stop-color="#c7682c"/><stop offset="1" stop-color="#5a2415"/></linearGradient>
    <linearGradient id="hComedy" x1="0" y1="0" x2="0" y2="1"><stop offset="0" stop-color="#e9c46a"/><stop offset="1" stop-color="#a0701e"/></linearGradient>
    <linearGradient id="hTheatre" x1="0" y1="0" x2="0" y2="1"><stop offset="0" stop-color="#8a1d22"/><stop offset="1" stop-color="#2b0709"/></linearGradient>
    <linearGradient id="hSport" x1="0" y1="0" x2="0" y2="1"><stop offset="0" stop-color="#4f8a3a"/><stop offset="1" stop-color="#1e3a18"/></linearGradient>
    <linearGradient id="hFamily" x1="0" y1="0" x2="0" y2="1"><stop offset="0" stop-color="#d8652f"/><stop offset="1" stop-color="#6b2a16"/></linearGradient>
  </defs>
  <g role="img" aria-label="Music festival crowd"><polygon points="268,50 336,89 336,167 268,206 200,167 200,89" fill="url(#hMusic)"/><text x="268" y="150">Music</text><text x="268" y="166">Events</text></g>
  <g role="img" aria-label="Comedy stage spotlight"><polygon points="432,50 500,89 500,167 432,206 364,167 364,89" fill="url(#hComedy)"/><text x="432" y="150">Top</text><text x="432" y="166">Comedy</text></g>
  <g role="img" aria-label="Theatre stage with red curtains"><polygon points="600,10 686,60 686,160 600,210 514,160 514,60" fill="url(#hTheatre)"/><text x="600" y="120">Theater</text><text x="600" y="136">Shows</text></g>
  <g role="img" aria-label="Football on a pitch"><polygon points="768,50 836,89 836,167 768,206 700,167 700,89" fill="url(#hSport)"/><text x="768" y="150">Sporting</text><text x="768" y="166">Events</text></g>
  <g role="img" aria-label="Family day out at a fair"><polygon points="932,50 1000,89 1000,167 932,206 864,167 864,89" fill="url(#hFamily)"/><text x="932" y="150">Family</text><text x="932" y="166">Attractions</text></g>
</svg>

<!-- reviews -->
<section class="reviews">
  <div class="sec-head" style="top:40px">
    <h2>Our Reviews</h2>
    <p>Lorem Ipsum is simply dummy text of the printing and typesetting industry. Lorem Ipsum has been the industry's standard dummy text ever since the 1500s.</p>
    <span class="btn">View All →</span>
  </div>
  <div class="vouch">
    <div class="name"><i></i>Vouch Ledger</div>
    <div class="score">★★★★★</div>
    <div class="total">Total <b style="color:var(--orange)">4500</b> Reviews</div>
  </div>
  <span class="chev" style="left:500px">‹</span>
  <div class="review" style="left:532px">
    <div class="avatar" role="img" aria-label="Reviewer portrait"></div>
    <h4>Sam Reed</h4>
    <div class="rate">★★★★★</div>
    <p>Great tickets and an easy booking flow. The event was amazing and entry was quick and smooth for our whole group.</p>
    <div class="more">READ MORE</div>
  </div>
  <div class="review" style="left:742px">
    <div class="avatar" role="img" aria-label="Reviewer portrait"></div>
    <h4>Lara Quinn</h4>
    <div class="rate">★★★★★</div>
    <p>Found exclusive seats I could not get anywhere else. Friendly support and fast delivery of my tickets by email.</p>
    <div class="more">READ MORE</div>
  </div>
  <span class="chev" style="left:952px">›</span>
</section>

<!-- about -->
<section class="about">
  <h2>Lorem Ipsum is simply dummy text of the printing and typesetting ..</h2>
  <p>It is a long established fact that a reader will be distracted by the readable content of a page when looking at its layout. The point of using Lorem Ipsum is that it has a more-or-less normal distribution of letters, as opposed to using 'Content here, content here', making it look like readable English. Many desktop publishing packages and web page editors now use Lorem Ipsum as their default model text.</p>
  <p>It is a long established fact that a reader will be distracted by the readable content of a page when looking at its layout. The point of using Lorem Ipsum is that it has a more-or-less normal distribution of letters, as opposed to using content here.</p>
  <span class="btn">Read More</span>
</section>
<div class="about-frame"></div>
<div class="about-photo" role="img" aria-label="Two women smiling while looking at a laptop"></div>

<!-- footer -->
<footer class="footer" role="img" aria-label="Festival crowd silhouetted against warm stage lights">
  <div class="brand"><span class="dot"></span>Gatepass Pro</div>
  <h3 style="left:210px">Quick Links</h3>
  <ul class="links" style="left:210px"><li>Home</li><li>About Us</li><li>Local Tickets</li><li>Advertise With Us</li><li>Jobs</li><li>Contact Us</li><li>FAQs</li></ul>
  <ul class="links" style="left:400px"><li>Home</li><li>About Us</li><li>Event Tickets</li><li>Advertise With Us</li><li>Jobs</li><li>Contact Us</li><li>FAQs</li></ul>
  <ul class="links" style="left:590px"><li>Home</li><li>About Us</li><li>Local Tickets</li><li>Advertise With Us</li><li>Jobs</li><li>Contact Us</li><li>FAQs</li></ul>
  <h3 style="left:800px">Contact Us</h3>
  <ul class="contact">
    <li><svg width="14" height="18" viewBox="0 0 14 18"><path d="M7 1a6 6 0 0 0-6 6c0 4.5 6 10 6 10s6-5.5 6-10a6 6 0 0 0-6-6z" fill="#f26522"/><circle cx="7" cy="7" r="2.2" fill="#fff"/></svg>12 Harbour Lane, Riverton</li>
    <li><svg width="16" height="12" viewBox="0 0 16 12"><rect x="1" y="1" width="14" height="10" fill="none" stroke="#f26522" stroke-width="1.5"/><path d="M1 1l7 6 7-6" fill="none" stroke="#f26522" stroke-width="1.5"/></svg>hello@gatepasspro.example</li>
    <li><svg width="14" height="14" viewBox="0 0 14 14"><path d="M3 1l3 3-2 2a8 8 0 0 0 4 4l2-2 3 3-2 2C6 13 1 8 1 3z" fill="#f26522"/></svg>+00 000 000 000</li>
  </ul>
  <div class="fsocial"><span>P</span><span>C</span><span>W</span><span>S</span></div>
  <div class="copy">© 2024 <b>Gatepass Pro</b> All Rights Reserved</div>
</footer>

</body>
</html>
```